New Business Card Design Project

We are a spa looking to create a professional elegant business card for a spa mainly black and white with a splash of lime green. This card will be two sided - the front side will have an image, the logo, and the spa's information - the back side will have a promotion for new customers - NEW CUSTOMERS $20 OFF

Look and feel: chic, modern, and spa-ish.
Information to be included:
Therapist Name
Therapist specialty
Address: 5147 Marlowe Ave, Beverly Hills CA 90211
Phone: (310) 482-3961

Let me know if you have any questions!

Thank you

```html
<!DOCTYPE html>
<html lang="en">
<head>
<meta charset="utf-8">
<title>Lumen Day Spa – Business Card</title>
<link rel="stylesheet" href="https://fonts.googleapis.com/css2?family=Arimo:wght@400&family=Parisienne&display=swap">
<style>
  :root {
    --ink: #111111;
    --paper: #ffffff;
    --lime: #8dc63f;
    --backdrop: #eef2ea;
    --card-shadow: rgba(0, 0, 0, 0.22);
  }
  * { box-sizing: border-box; margin: 0; padding: 0; }
  html, body {
    width: 1200px;
    height: 1000px;
    overflow: hidden;
    background: var(--backdrop);
  }
  .canvas {
    position: relative;
    width: 1200px;
    height: 1000px;
  }
  .card {
    position: absolute;
    width: 760px;
    height: 430px;
    background: var(--paper);
    border-radius: 40px;
    overflow: hidden;
    box-shadow: 0 6px 18px var(--card-shadow);
    font-family: "Arimo", Arial, sans-serif;
    color: var(--ink);
  }
  .card--front { left: 60px; top: 60px; }
  .card--back { left: 380px; top: 510px; }

  .card__band {
    position: absolute;
    left: 0; right: 0; bottom: 0;
    height: 92px;
    background: var(--ink);
    border-top: 8px solid var(--lime);
    display: flex;
    align-items: center;
    justify-content: center;
  }
  .card__web {
    color: var(--paper);
    font-size: 30px;
    letter-spacing: 0.42em;
    padding-left: 0.42em;
  }

  .brand {
    position: absolute;
    left: 50px;
    top: 120px;
    display: flex;
    align-items: center;
    gap: 16px;
  }
  .brand__dot {
    width: 44px;
    height: 44px;
    border: 5px solid var(--ink);
    border-radius: 50%;
  }
  .brand__name {
    font-size: 30px;
    letter-spacing: 0.08em;
    color: var(--ink);
    line-height: 1.15;
  }

  .contact {
    position: absolute;
    right: 70px;
    top: 60px;
    text-align: right;
  }
  .contact__name {
    font-family: "Parisienne", cursive;
    font-size: 44px;
    line-height: 1.1;
  }
  .contact__role {
    font-family: "Parisienne", cursive;
    font-size: 30px;
    color: var(--lime);
    margin-bottom: 26px;
  }
  .contact__line { font-size: 23px; line-height: 1.45; }
  .contact__rule {
    height: 2px;
    width: 310px;
    margin: 10px 0 20px auto;
    background: var(--lime);
  }
  .contact__address { font-size: 20px; line-height: 1.5; }

  .promo {
    position: absolute;
    right: 60px;
    top: 80px;
    text-align: center;
  }
  .promo__title {
    font-family: "Parisienne", cursive;
    font-size: 38px;
  }
  .promo__offer {
    font-family: "Parisienne", cursive;
    font-size: 100px;
    color: var(--lime);
    line-height: 1.4;
  }
</style>
</head>
<body>
<main class="canvas">

  <section class="card card--front" aria-label="Business card front">
    <div class="brand">
      <span class="brand__dot"></span>
      <span class="brand__name">LUMEN<br>DAY SPA</span>
    </div>
    <div class="contact">
      <p class="contact__name">Clara Vance</p>
      <p class="contact__role">Makeup Specialist</p>
      <p class="contact__line">(310) 482-3961</p>
      <p class="contact__line">contact@lumendayspa.com</p>
      <div class="contact__rule"></div>
      <p class="contact__address">5147 Marlowe Ave<br>Beverly Hills CA 90211</p>
    </div>
    <div class="card__band"><span class="card__web">lumendayspa.com</span></div>
  </section>

  <section class="card card--back" aria-label="Business card back">
    <div class="brand">
      <span class="brand__dot"></span>
      <span class="brand__name">LUMEN<br>DAY SPA</span>
    </div>
    <div class="promo">
      <p class="promo__title">New Customer Special!</p>
      <p class="promo__offer">$20 Off</p>
    </div>
    <div class="card__band"><span class="card__web">lumendayspa.com</span></div>
  </section>

</main>
</body>
</html>
```